Business card for senior move management company
@ Project Holder : Could you extend this contest,please?
Is there latitude with the logo, can we remove the wavy lines if they interfere with the design?
All
there are some excellent design choices already, thank you!
General comments are:
1. The client has asked for her name to be in all capitals with the first letter of each word slightly larger than the rest.
2. The client for this company serves are tyically over 75 years old. The fonts need to be clearly legible, and as large as is practical. The phone number is especially important for size.
3. Vhange from the original spec: the website address should go with the text "Organizing, Downsizing and relocation management"
4. the text "Lowell, MA" should go with the phone number and email.
We are still interested in seeing additional creative ideas.
Thanks Again!
Gareth

```html
<!DOCTYPE html>
<html lang="en">
<head>
<meta charset="utf-8">
<title>Gentle Path Moves – Business Card</title>
<link href="https://fonts.googleapis.com/css2?family=Tinos:wght@400;700&display=swap" rel="stylesheet">
<style>
  :root {
    --page: #e9e6e1;
    --card-black: #0b0b0c;
    --blue-deep: #0f4f98;
    --blue-mid: #1a6fc4;
    --blue-light: #3a8fe0;
    --white: #ffffff;
    --ring-tone: #2a2a2e;
    --shadow: rgba(0,0,0,0.25);
  }
  * { margin: 0; padding: 0; box-sizing: border-box; }
  html, body { width: 1200px; height: 921px; overflow: hidden; }
  body {
    background: var(--page);
    font-family: "Tinos", "Times New Roman", serif;
    color: var(--white);
    position: relative;
  }
  .card {
    position: absolute;
    width: 540px;
    height: 309px;
    top: 306px;
    box-shadow: 0 6px 18px var(--shadow);
    overflow: hidden;
    background: var(--card-black);
  }
  .card--front { left: 40px; }
  .card--back { left: 620px; }

  /* Front */
  .front__brand-panel {
    position: absolute; left: 0; top: 0; width: 48%; height: 100%;
    background: linear-gradient(160deg, var(--blue-light) 0%, var(--blue-mid) 45%, var(--blue-deep) 100%);
  }
  .brand {
    position: absolute; display: flex; align-items: center; gap: 10px;
  }
  .brand__dot {
    width: 22px; height: 22px; border: 3px solid var(--white); border-radius: 50%; flex: none;
  }
  .brand__name { font-size: 22px; font-weight: 700; line-height: 1.05; }
  .front__brand { left: 24px; top: 32px; }
  .front__services {
    position: absolute; left: 24px; bottom: 22px;
    font-size: 17px; font-weight: 700; line-height: 1.2;
  }
  .front__services .web { display: block; margin-top: 2px; }
  .front__ornament {
    position: absolute; right: 0; top: 0; width: 52%; height: 58%;
    background: radial-gradient(circle at 78% 20%, var(--ring-tone) 0%, var(--card-black) 70%);
  }
  .contact {
    position: absolute; left: 52%; top: 112px; padding-left: 20px;
  }
  .contact__name { font-size: 26px; font-variant: small-caps; letter-spacing: 0.5px; line-height: 1; }
  .contact__title { font-size: 15px; margin-top: 3px; }
  .contact__phone { font-size: 31px; margin-top: 22px; line-height: 1; }
  .contact__email, .contact__city { font-size: 16px; line-height: 1.3; }
  .contact__email { margin-top: 4px; }

  /* Back */
  .back__tagline {
    position: absolute; left: 0; top: 0; width: 100%; height: 70px;
    padding: 20px 26px; font-size: 18px;
  }
  .back__band {
    position: absolute; left: 0; top: 70px; width: 100%; height: 170px;
    background: linear-gradient(180deg, var(--blue-light) 0%, var(--blue-mid) 50%, var(--blue-deep) 100%);
  }
  .back__brand { left: 40px; top: 66px; }
  .back__ornament {
    position: absolute; right: 0; top: 30px; width: 190px; height: 240px;
    background: radial-gradient(circle at 70% 50%, rgba(255,255,255,0.22) 0%, rgba(255,255,255,0) 65%);
  }
  .back__web {
    position: absolute; right: 26px; bottom: 24px; font-size: 17px; font-weight: 700;
  }
</style>
</head>
<body>
  <section class="card card--front">
    <div class="front__brand-panel">
      <div class="brand front__brand">
        <span class="brand__dot"></span>
        <span class="brand__name">Gentle Path Moves</span>
      </div>
      <p class="front__services">Organizing, Downsizing &amp;<br>Relocation Management<span class="web">www.GPMtransitions.com</span></p>
    </div>
    <div class="front__ornament" role="img" aria-label="Postmark rings and cancellation lines decoration"></div>
    <div class="contact">
      <p class="contact__name">Maren Holt</p>
      <p class="contact__title">President</p>
      <p class="contact__phone">555.014.2233</p>
      <p class="contact__email">Maren@GPMtransitions.com</p>
      <p class="contact__city">Lowell, MA</p>
    </div>
  </section>

  <section class="card card--back">
    <p class="back__tagline">You and Your Belongings on a Gentle Path</p>
    <div class="back__band">
      <div class="brand back__brand">
        <span class="brand__dot"></span>
        <span class="brand__name">Gentle Path Moves</span>
      </div>
    </div>
    <div class="back__ornament" role="img" aria-label="Postmark rings decoration"></div>
    <p class="back__web">www.GPMtransitions.com</p>
  </section>
</body>
</html>
```